website for film and theater production company

I am looking for a creative splash page that has the elements to create new pages or layers of pages for each project our company is working on. We have some elements that we really like, including our logo, posters for the projects, and one shutter stock graphic purchased - could be used or not used but i do like it. I have attached a powerpoint file with some of the visions in my head that use all the elements - potential ideas that i have no way of knowing how to carry out. I would like the web design to be able to run on wordpress. I would like the site to be beautiful and clean and creative - and cannot figure out how to do a successful MENU bar. Menu items would include: About Us, and then perhaps a tab for each of the three projects represented by the posters, and a tickets online tab, and a products tab. I also would like a special tab or button for The Blog which covers all of Lantern MossCreative, not just each project. Clutter is my enemy. Thank you for your help.
Updates

Project Deadline Extended
Reason: i will be out of town the rest of the week and off the grid and do not want to rush. I will try to finalize my choice on Monday June 6. Thank you.

Target Market(s)

this is a digital resume for people interested in the projects our creative agency has going. I need to be able to change projects that are in the limelight, but that is not often as these are long term projects. It will also be used as a place to sell tickets online to our theatre productions, and products that arise from them.

Industry/Entity Type

It Company

Number of Pages Required

1 page

Requirements
Must have
• a sense of awe and excitement looking at it -- I am not interested in pro forma web design or things that look corporate. This is a creative arts agency!
Nice to have
• Color, emotion, clarity
Should not have
• too busy, hard to figure out how to use.

```html
<!DOCTYPE html>
<html lang="en">
<head>
<meta charset="utf-8">
<title>Lantern Moss Creative — Film &amp; Theatre Production</title>
<link href="https://fonts.googleapis.com/css2?family=Rokkitt:wght@500;700;800&family=Open+Sans:wght@400;600&family=Roboto:wght@400;500&display=swap" rel="stylesheet">
<style>
:root{
  --red:#d12a2f;
  --red-deep:#b81f25;
  --ink:#222222;
  --text:#555555;
  --muted:#8a8a8a;
  --light:#f3f3f3;
  --white:#ffffff;
  --footer:#232323;
  --footer-deep:#141414;
  --line:#e2e2e2;
}
*{margin:0;padding:0;box-sizing:border-box}
html,body{width:1200px;height:2941px;overflow:hidden;background:var(--white)}
body{position:relative;font-family:"Open Sans",Arial,sans-serif;color:var(--text)}
.display{font-family:"Rokkitt",Georgia,serif;font-weight:800;text-transform:uppercase;letter-spacing:.5px;white-space:nowrap}
a{color:inherit;text-decoration:none}

/* header */
.site-header{position:absolute;left:0;top:0;width:1200px;height:124px;background:var(--white)}
.brand{position:absolute;left:100px;top:28px;display:flex;align-items:center;gap:10px}
.brand-mark{width:22px;height:22px;background:var(--red);border-radius:50%}
.brand-name{font-family:"Rokkitt",Georgia,serif;font-weight:800;font-size:28px;color:var(--red);line-height:1;white-space:nowrap}
.brand-name small{display:block;font-size:17px;letter-spacing:3px;text-transform:uppercase}
.call{position:absolute;right:100px;top:22px;display:flex;align-items:center;gap:10px;font-family:"Roboto",Arial,sans-serif;font-size:15px;color:var(--red)}
.call-icon{width:26px;height:26px;border-radius:50%;background:var(--red);display:flex;align-items:center;justify-content:center}
.main-nav{position:absolute;right:100px;top:64px;display:flex;align-items:center;font-family:"Rokkitt",Georgia,serif;font-weight:700;font-size:12px;letter-spacing:1px;color:#444;white-space:nowrap}
.main-nav a{padding:7px 17px;border-right:1px solid var(--line)}
.main-nav a:last-of-type{border-right:none}
.main-nav a.is-active{color:var(--red);border:2px solid var(--red);border-radius:3px;margin-right:8px}
.main-nav .search{margin-left:12px;display:flex}

/* hero */
.hero{position:absolute;left:0;top:124px;width:1200px;height:553px;background:radial-gradient(ellipse at 70% 45%,#6e5a72 0%,#3a2a2c 35%,#1a1212 70%,#0d0a0a 100%)}
.hero-title{position:absolute;left:100px;top:196px;font-size:38px;line-height:46px;color:var(--white)}
.hero-sub{position:absolute;left:100px;top:290px;font-size:14px;line-height:24px;color:#eee}
.btn-red{position:absolute;left:100px;top:366px;width:196px;height:40px;background:var(--red);color:var(--white);font-family:"Rokkitt",Georgia,serif;font-weight:700;font-size:14px;letter-spacing:1px;display:flex;align-items:center;justify-content:center;border-radius:2px}
.hero-arrow{position:absolute;top:270px}

/* about */
.about{position:absolute;left:0;top:677px;width:1200px;height:465px;background:linear-gradient(135deg,#f6f6f6,#ececec)}
.video-frame{position:absolute;left:100px;top:85px;width:497px;height:293px;border:2px solid var(--red);background:linear-gradient(110deg,#2e8fb8,#e9c93d 35%,#d8475a 60%,#7cc06d 85%,#3f5fb0)}
.video-bar{position:absolute;left:14px;right:14px;bottom:14px;height:18px;background:rgba(0,0,0,.55)}
.video-progress{position:absolute;left:0;top:7px;width:52%;height:4px;background:#e3c43a}
.video-play{position:absolute;left:213px;top:125px;width:62px;height:38px;background:var(--red);border-radius:6px;display:flex;align-items:center;justify-content:center}
.about-text{position:absolute;left:630px;top:92px;width:470px}
.about-text h2{font-size:32px;color:var(--ink);line-height:36px}
.about-text h3{font-family:"Rokkitt",Georgia,serif;font-weight:700;font-size:22px;color:var(--ink);margin:6px 0 14px}
.about-text p{font-size:11px;line-height:19px;color:#666;margin-bottom:14px}
.btn-dark{display:inline-flex;align-items:center;justify-content:center;width:112px;height:36px;background:#2d2d2d;color:var(--white);font-family:"Rokkitt",Georgia,serif;font-weight:700;font-size:13px;letter-spacing:1px;border-radius:3px;margin-top:6px}

/* section heads */
.section-head{position:absolute;left:0;width:1200px;display:flex;justify-content:center;align-items:center;gap:24px}
.section-badge{display:flex;align-items:center;justify-content:center;font-size:29px;padding:0 18px;height:62px;border-radius:6px}
.stars{color:var(--white);font-size:13px;letter-spacing:6px;white-space:nowrap}

/* services */
.services{position:absolute;left:0;top:1142px;width:1200px;height:488px;background:var(--red)}
.services-decor{position:absolute;left:30px;top:70px;width:280px;height:320px;background:radial-gradient(circle,rgba(0,0,0,.16),rgba(0,0,0,0) 70%)}
.services .section-head{top:45px}
.services .section-badge{border:3px solid var(--white);color:var(--white)}
.service{position:absolute;top:155px;width:250px;text-align:center;color:var(--white)}
.service-icon{width:112px;height:112px;margin:0 auto;border-radius:50%;background:#2b2b2b;border:4px solid rgba(255,255,255,.85);display:flex;align-items:center;justify-content:center}
.service h4{font-family:"Rokkitt",Georgia,serif;font-weight:800;font-size:17px;letter-spacing:.3px;margin:38px 0 8px;text-transform:uppercase;white-space:nowrap}
.service p{font-size:11px;line-height:19px;padding:0 14px}
.service .more{display:inline-block;margin-top:12px;font-size:11px;text-decoration:underline}

/* shows */
.shows .section-head{top:1678px}
.shows .section-badge{border:3px solid var(--red);color:#333}
.show{position:absolute;top:1788px;width:314px}
.show-poster{width:314px;height:256px;border:4px solid #eeeeee}
.show h5{font-family:"Roboto",Arial,sans-serif;font-weight:500;font-size:16px;color:var(--ink);margin-top:18px}
.show p{font-size:11px;line-height:19px;color:#666;width:270px;margin-top:6px}
.show-next{position:absolute;right:0;top:312px;width:28px;height:28px;border:2px solid #e0608c;border-radius:50%;display:flex;align-items:center;justify-content:center}

/* news */
.news-heading{position:absolute;left:98px;top:2190px;font-size:25px;color:#333}
.news-item{position:absolute;left:98px;width:660px}
.news-thumb{position:absolute;left:0;top:0;width:229px;height:122px;border:4px solid #eeeeee}
.news-body{position:absolute;left:257px;top:-6px;width:410px}
.news-body h6{font-family:"Roboto",Arial,sans-serif;font-weight:400;font-size:16px;color:#444}
.news-date{font-family:"Rokkitt",Georgia,serif;font-weight:700;font-size:13px;color:var(--red);margin:14px 0 8px}
.news-body p{font-size:10.5px;line-height:19px;color:#666}
.news-feature{position:absolute;left:810px;top:2215px;width:292px;height:317px;background:linear-gradient(160deg,#d8202a 0%,#b4171d 35%,#f0c21d 60%,#1b1b1b 85%)}

/* footer */
.rainbow{position:absolute;left:0;top:2608px;width:1200px;height:4px;background:linear-gradient(90deg,#d12a2f,#e06b2b,#3a8f3d,#2f6fb5,#7b3fa0,#d12a2f)}
.site-footer{position:absolute;left:0;top:2612px;width:1200px;height:268px;background:var(--footer);color:#cfcfcf}
.footer-brand{position:absolute;left:100px;top:92px;width:225px;height:72px;border:3px solid var(--white);border-radius:6px;display:flex;align-items:center;justify-content:center;flex-direction:column;font-family:"Rokkitt",Georgia,serif;font-weight:800;color:var(--white);font-size:24px;line-height:26px;white-space:nowrap}
.footer-col{position:absolute;top:55px}
.footer-col h6{font-family:"Roboto",Arial,sans-serif;font-weight:500;font-size:16px;color:var(--white);letter-spacing:.5px;margin-bottom:22px;text-transform:uppercase}
.contact-line{display:flex;align-items:flex-start;gap:14px;font-size:13px;line-height:20px;margin-bottom:14px}
.post{display:flex;gap:12px;font-size:11px;line-height:18px;margin-bottom:16px;width:240px}
.post b{color:var(--red);font-weight:400}
.post small{display:block;color:#999;font-size:11px;margin-top:4px}
.social-line{display:flex;align-items:center;gap:10px;font-size:13px;margin-bottom:14px}
.social-dot{width:24px;height:24px;border:1.5px solid #bbb;border-radius:50%}
.copyright{position:absolute;left:0;top:2880px;width:1200px;height:61px;background:var(--footer-deep);color:#bbb;font-size:11px;display:flex;align-items:center;justify-content:center}
</style>
</head>
<body>

<header class="site-header">
  <a class="brand" href="#">
    <span class="brand-mark"></span>
    <span class="brand-name">Lantern Moss<small>Creative</small></span>
  </a>
  <div class="call">
    <span class="call-icon"><svg width="13" height="13" viewBox="0 0 24 24"><path fill="#fff" d="M6.6 10.8a15.1 15.1 0 0 0 6.6 6.6l2.2-2.2c.3-.3.7-.4 1-.2 1.1.4 2.3.6 3.6.6.6 0 1 .4 1 1V20c0 .6-.4 1-1 1C10.6 21 3 13.4 3 4c0-.6.4-1 1-1h3.5c.6 0 1 .4 1 1 0 1.3.2 2.5.6 3.6.1.3 0 .7-.2 1z"/></svg></span>
    Call us (+) 555-310-4821
  </div>
  <nav class="main-nav">
    <a class="is-active" href="#">HOME</a>
    <a href="#">ABOUT US</a>
    <a href="#">FILM / PRODUCTION</a>
    <a href="#">PROMOTING SHOWS</a>
    <a href="#">CONTACT US</a>
    <span class="search"><svg width="14" height="14" viewBox="0 0 24 24"><circle cx="10" cy="10" r="6.5" fill="none" stroke="#555" stroke-width="2.5"/><path d="M15 15l6 6" stroke="#555" stroke-width="2.5"/></svg></span>
  </nav>
</header>

<section class="hero" role="img" aria-label="Photograph of a packed theatre auditorium facing a lit stage with curtains">
  <svg class="hero-arrow" style="left:34px" width="24" height="60" viewBox="0 0 24 60"><path d="M20 2L4 30l16 28" fill="none" stroke="#fff" stroke-width="2"/></svg>
  <svg class="hero-arrow" style="right:34px" width="24" height="60" viewBox="0 0 24 60"><path d="M4 2l16 28L4 58" fill="none" stroke="#fff" stroke-width="2"/></svg>
  <h1 class="hero-title display">We are a film &amp;<br>theatre production</h1>
  <p class="hero-sub">Performing arts and film writing, directing, and producing<br>Committed to creativity, community, and healing</p>
  <a class="btn-red" href="#">VIEW MORE INFO</a>
</section>

<section class="about">
  <div class="video-frame" role="img" aria-label="Video still of a colourful painted poster with two portraits">
    <div class="video-play"><svg width="18" height="20" viewBox="0 0 18 20"><path d="M2 1l15 9-15 9z" fill="#fff"/></svg></div>
    <div class="video-bar"><div class="video-progress"></div></div>
  </div>
  <div class="about-text">
    <h2 class="display">About our company</h2>
    <h3>Lantern Moss Creative</h3>
    <p>Lorem ipsum dolor sit amet, consectetur adipiscing elit, sed do eiusmod tempor incididunt ut labore et dolore magna aliqua. Ut enim ad minim veniam, quis nostrud exercitation ullamco laboris nisi ut aliquip ex ea commodo consequat. Duis aute irure dolor in enderit in voluptate velit esse cillum dolore eu fugiat nulla pariatur. Excepteur sint occaecat cupidatat non proident,</p>
    <p>Lorem ipsum dolor sit amet, consectetur adipiscing elit, sed do eiusmod tempor incididunt ut labore et dolore magna aliqua. Ut enim ad minim veniam, quis</p>
    <a class="btn-dark" href="#">READ MORE</a>
  </div>
</section>

<section class="services">
  <div class="services-decor" role="img" aria-label="Faint film projector illustration"></div>
  <div class="section-head">
    <span class="stars">★★★</span>
    <h2 class="section-badge display">Our services</h2>
    <span class="stars">★★★</span>
  </div>

  <div class="service" style="left:77px">
    <div class="service-icon"><svg width="40" height="40" viewBox="0 0 40 40"><rect x="4" y="6" width="32" height="22" rx="2" fill="none" stroke="#fff" stroke-width="2.5"/><path d="M15 34h10M20 28v6" stroke="#fff" stroke-width="2.5"/></svg></div>
    <h4>Film writing</h4>
    <p>Lorem ipsum dolor sit amet, consectetur adipiscing elit, sed do eiusmod tempor incididunt ut labore et dolore</p>
    <a class="more" href="#">READ MORE</a>
  </div>
  <div class="service" style="left:344px">
    <div class="service-icon"><svg width="44" height="40" viewBox="0 0 44 40"><circle cx="16" cy="18" r="11" fill="none" stroke="#fff" stroke-width="2.5"/><circle cx="28" cy="22" r="11" fill="none" stroke="#fff" stroke-width="2.5"/></svg></div>
    <h4>Performing arts</h4>
    <p>Lorem ipsum dolor sit amet, consectetur adipiscing elit, sed do eiusmod tempor incididunt ut labore et dolore</p>
    <a class="more" href="#">READ MORE</a>
  </div>
  <div class="service" style="left:610px">
    <div class="service-icon"><svg width="40" height="40" viewBox="0 0 40 40"><rect x="5" y="16" width="30" height="18" fill="none" stroke="#fff" stroke-width="2.5"/><path d="M5 9l29-4 1 7-29 4z" fill="none" stroke="#fff" stroke-width="2.5"/><path d="M12 8l4 6M20 7l4 6M28 6l3 5" stroke="#fff" stroke-width="2"/></svg></div>
    <h4>Directing</h4>
    <p>Lorem ipsum dolor sit amet, consectetur adipiscing elit, sed do eiusmod tempor incididunt ut labore et dolore</p>
    <a class="more" href="#">READ MORE</a>
  </div>
  <div class="service" style="left:869px">
    <div class="service-icon"><svg width="42" height="42" viewBox="0 0 42 42"><circle cx="21" cy="21" r="16" fill="none" stroke="#fff" stroke-width="2.5"/><circle cx="21" cy="21" r="8" fill="none" stroke="#fff" stroke-width="2.5"/><path d="M21 2v10M21 30v10M2 21h10M30 21h10" stroke="#fff" stroke-width="2.5"/></svg></div>
    <h4>Producing committed</h4>
    <p>Lorem ipsum dolor sit amet, consectetur adipiscing elit, sed do eiusmod tempor incididunt ut labore et dolore</p>
    <a class="more" href="#">READ MORE</a>
  </div>
</section>

<section class="shows">
  <div class="section-head">
    <h2 class="section-badge display">Promoting shows</h2>
  </div>
  <article class="show" style="left:98px">
    <div class="show-poster" role="img" aria-label="Film poster with a child seated on a suitcase" style="background:linear-gradient(160deg,#f1ece4,#d9cfc2 60%,#b9a99a)"></div>
    <h5>Feature filmscript</h5>
    <p>Lorem ipsum dolor sit amet, consectetur ading elit, sed do eiusmod tempor incididunt</p>
    <span class="show-next"><svg width="10" height="12" viewBox="0 0 10 12"><path d="M2 1l6 5-6 5" fill="none" stroke="#e0608c" stroke-width="2"/></svg></span>
  </article>
  <article class="show" style="left:440px">
    <div class="show-poster" role="img" aria-label="Colourful watercolour poster of a touring production cast" style="background:linear-gradient(135deg,#f4e7c8,#e4b03e 30%,#d2454f 55%,#5aa6c9 80%,#7bbf6a)"></div>
    <h5>Touring production</h5>
    <p>Lorem ipsum dolor sit amet, consectetur ading elit, sed do eiusmod tempor incididunt</p>
    <span class="show-next"><svg width="10" height="12" viewBox="0 0 10 12"><path d="M2 1l6 5-6 5" fill="none" stroke="#e0608c" stroke-width="2"/></svg></span>
  </article>
  <article class="show" style="left:786px">
    <div class="show-poster" role="img" aria-label="Photograph of a smiling woman holding a framed picture" style="background:linear-gradient(150deg,#6b4a36,#a77a5a 45%,#d7b190 70%,#e9e2d8)"></div>
    <h5>Film with development package</h5>
    <p>Lorem ipsum dolor sit amet, consectetur ading elit, sed do eiusmod tempor incididunt</p>
    <span class="show-next"><svg width="10" height="12" viewBox="0 0 10 12"><path d="M2 1l6 5-6 5" fill="none" stroke="#e0608c" stroke-width="2"/></svg></span>
  </article>
</section>

<section class="news">
  <h2 class="news-heading display">Latest news</h2>
  <article class="news-item" style="top:2245px">
    <div class="news-thumb" role="img" aria-label="Photograph of a dancer leaping against a pale sky" style="background:linear-gradient(180deg,#b9cfcf,#7f9a94 60%,#4b5a48)"></div>
    <div class="news-body">
      <h6>Nulla at diam ornare, aliquam urna vel,</h6>
      <div class="news-date">JUNE 25, 2015</div>
      <p>Nulla at diam ornare, aliquam urna vel, commodo urna. Nam id risus a est luctus consectetur quis eget libero. Suspendisse potenti. Pellentesque habitant morbi tristique senectus et netus et malesuada fames</p>
    </div>
  </article>
  <article class="news-item" style="top:2416px">
    <div class="news-thumb" role="img" aria-label="Photograph of two performers outdoors at dusk" style="background:linear-gradient(180deg,#c9c2b6,#6e6660 55%,#2e2a28)"></div>
    <div class="news-body">
      <h6>Nulla at diam ornare, aliquam urna vel,</h6>
      <div class="news-date">JUNE 25, 2015</div>
      <p>Nulla at diam ornare, aliquam urna vel, commodo urna. Nam id risus a est luctus consectetur quis eget libero. Suspendisse potenti. Pellentesque habitant morbi tristique senectus et netus et malesuada fames</p>
    </div>
  </article>
  <div class="news-feature" role="img" aria-label="Illustration of clasped hands painted in red, yellow and black"></div>
</section>

<div class="rainbow"></div>
<footer class="site-footer">
  <div class="footer-brand">Lantern Moss<span style="font-size:17px;letter-spacing:3px">CREATIVE</span></div>

  <div class="footer-col" style="left:390px">
    <h6>Contacts</h6>
    <div class="contact-line"><svg width="12" height="16" viewBox="0 0 12 16"><path d="M6 0a6 6 0 0 0-6 6c0 4.5 6 10 6 10s6-5.5 6-10a6 6 0 0 0-6-6zm0 8.5A2.5 2.5 0 1 1 6 3.5a2.5 2.5 0 0 1 0 5z" fill="#aaa"/></svg><span>218 Lantern Moss Lane<br>Riverbend Valley 40812</span></div>
    <div class="contact-line"><svg width="13" height="13" viewBox="0 0 24 24"><path fill="#aaa" d="M6.6 10.8a15.1 15.1 0 0 0 6.6 6.6l2.2-2.2c.3-.3.7-.4 1-.2 1.1.4 2.3.6 3.6.6.6 0 1 .4 1 1V20c0 .6-.4 1-1 1C10.6 21 3 13.4 3 4c0-.6.4-1 1-1h3.5c.6 0 1 .4 1 1 0 1.3.2 2.5.6 3.6.1.3 0 .7-.2 1z"/></svg><span>Call Us: +555-310-4821</span></div>
    <div class="contact-line"><svg width="14" height="11" viewBox="0 0 14 11"><rect x="0" y="0" width="14" height="11" fill="#aaa"/><path d="M0 0l7 6 7-6" fill="none" stroke="#232323" stroke-width="1.3"/></svg><span>hello@lanternmosscreative.com</span></div>
  </div>

  <div class="footer-col" style="left:682px">
    <h6>Latest posts</h6>
    <div class="post"><svg width="16" height="16" viewBox="0 0 16 16" style="flex:none"><rect width="16" height="16" rx="2" fill="#ddd"/></svg><div><b>@Lantern Moss Creative</b> Fusce susct varius mi. Cum sociis natoque penatibus<small>1 day ago</small></div></div>
    <div class="post"><svg width="16" height="16" viewBox="0 0 16 16" style="flex:none"><rect width="16" height="16" rx="2" fill="#ddd"/></svg><div><b>@Lantern Moss Creative</b> Fusce susct varius mi. Cum sociis natoque penatibus<small>1 day ago</small></div></div>
  </div>

  <div class="footer-col" style="left:983px">
    <h6>Social media</h6>
    <div class="social-line"><span class="social-dot"></span>Circleboard</div>
    <div class="social-line"><span class="social-dot"></span>Chirpline</div>
    <div class="social-line"><span class="social-dot"></span>Orbitnet</div>
  </div>
</footer>
<div class="copyright">© 2016 Lantern Moss Creative. All Rights Reserved.</div>

</body>
</html>
```